Property management company looking for modern card design

We at Blue Maple Holdings provides property management services for its residential and commercial properties, with expertise in all categories of multifamily, industrial and office projects throughout California.

We need a business card design that is professional and modern designed business card. In our field, clients get hundreds of business cards, we would like our card to stand out.

Please avoid small print.

Target Market(s)

Professionals and high end clients

Industry/Entity Type

Financial Planning

Contact Information for Business Card

Company Name: Blue Maple Holdings, Name, email, license #, phone number, website bluemapleholdings.example

Font styles to use
Sans Serif

Requirements
Must have
• The card design needs to be adaptable because there is a possibly we will be expanding into different sectors other than real estate. The card design should be focused on financial planning and asset management.
Nice to have
• Modern and simple business card. Eye catching. Non-standard size/shaped cards would be great.
• bluemapleholdings.example
Should not have
• Too many bright color or any pictures or shapes of real estate stuff.

```html
<!DOCTYPE html>
<html lang="en">
<head>
<meta charset="utf-8">
<title>Blue Maple Holdings – Business Card</title>
<link rel="stylesheet" href="https://fonts.googleapis.com/css2?family=Montserrat:wght@400;500;600;700&display=swap">
<style>
  :root {
    --bg-light: #f4f4f4;
    --bg-dark: #77777b;
    --card-cream: #f1efe1;
    --brand-red: #ec2232;
    --brand-maroon: #7a141a;
    --panel-charcoal: #2f2f2f;
    --ink: #2b2b2b;
    --ink-muted: #555555;
    --white: #ffffff;
  }
  html, body {
    margin: 0;
    padding: 0;
    width: 1200px;
    height: 1200px;
    overflow: hidden;
  }
  body {
    background: radial-gradient(circle at 50% 50%, var(--bg-light) 0%, #b9b9bb 45%, var(--bg-dark) 100%);
    font-family: "Montserrat", sans-serif;
  }
  .stage { display: block; width: 1200px; height: 1200px; }
  .card-cream { fill: var(--card-cream); }
  .band-red { fill: var(--brand-red); }
  .band-maroon { fill: var(--brand-maroon); }
  .panel-dark { fill: var(--panel-charcoal); }
  .mark-circle { fill: var(--brand-maroon); }
  .icon-box { fill: var(--panel-charcoal); }
  .icon-glyph { fill: var(--white); }
  .icon-line { fill: none; stroke: var(--white); stroke-width: 1.6; }
  .header-title {
    font-family: "Montserrat", sans-serif; font-weight: 500; font-size: 24px;
    letter-spacing: 3px; fill: var(--white); text-anchor: middle;
  }
  .brand-name {
    font-family: "Montserrat", sans-serif; font-weight: 500; font-size: 32px;
    letter-spacing: 4px; fill: var(--brand-red); text-anchor: middle;
  }
  .brand-name--small { font-size: 21px; letter-spacing: 3px; }
  .brand-url {
    font-family: "Montserrat", sans-serif; font-weight: 500; font-size: 15px;
    fill: var(--ink-muted); text-anchor: middle;
  }
  .brand-url--dim { font-size: 11px; fill: #7a7a7a; }
  .footer-email {
    font-family: "Montserrat", sans-serif; font-weight: 400; font-size: 19px;
    fill: var(--white); text-anchor: middle;
  }
  .person-name {
    font-family: "Montserrat", sans-serif; font-weight: 600; font-size: 40px;
    letter-spacing: 4px; fill: var(--white); text-anchor: middle;
  }
  .contact-line {
    font-family: "Montserrat", sans-serif; font-weight: 400; font-size: 14px;
    fill: var(--ink);
  }
</style>
</head>
<body>
<svg class="stage" viewBox="0 0 1200 1200" xmlns="http://www.w3.org/2000/svg" role="img" aria-label="Blue Maple Holdings business card, front and back">

  <!-- Front of card -->
  <g class="card-front" transform="translate(240 115.5)">
    <rect class="card-cream" x="0" y="0" width="720" height="432"/>
    <rect class="band-red" x="0" y="0" width="720" height="49.5"/>
    <polygon class="band-maroon" points="184.5,0 535.5,0 535.5,49.5 577.5,49.5 535.5,79.5 184.5,79.5 145.5,49.5 184.5,49.5"/>
    <text class="header-title" x="360" y="46">BLUE MAPLE</text>

    <circle class="mark-circle" cx="358.5" cy="192" r="48"/>
    <text class="brand-name" x="358.5" y="296">BLUE MAPLE</text>
    <text class="brand-url" x="358.5" y="323">www.bluemapleholdings.example</text>

    <rect class="band-red" x="0" y="399" width="720" height="33"/>
    <polygon class="band-maroon" points="169.5,384 544.5,384 583.5,432 135,432"/>
    <text class="footer-email" x="360" y="415">dana@bluemapleholdings.example</text>
  </g>

  <!-- Back of card -->
  <g class="card-back" transform="translate(240 612)">
    <rect class="card-cream" x="0" y="0" width="720" height="433.5"/>
    <rect class="panel-dark" x="0" y="0" width="358.5" height="433.5"/>

    <rect class="band-red" x="0" y="48" width="375" height="84"/>
    <polygon class="band-maroon" points="358.5,132 375,132 358.5,147"/>
    <text class="person-name" x="247.5" y="105">DANA</text>

    <circle class="mark-circle" cx="172.5" cy="246" r="36"/>
    <text class="brand-name brand-name--small" x="165" y="305">BLUE MAPLE</text>
    <text class="brand-url brand-url--dim" x="165" y="326">www.bluemapleholdings.example</text>

    <!-- Phone -->
    <g class="contact-row" transform="translate(397.5 192)">
      <rect class="icon-box" width="36" height="36"/>
      <path class="icon-glyph" d="M11 9.5c1.2-.8 2.2-.6 2.8.4l1.6 2.8c.5.9.2 1.6-.6 2.1l-1 .6c.9 2.3 2.5 4 4.8 4.9l.6-1c.5-.8 1.3-1 2.1-.6l2.8 1.6c1 .6 1.1 1.6.4 2.8-1.2 2-3.3 2.4-5.6 1.2-3.8-2-6.5-4.7-8.5-8.5-1.2-2.3-.9-4.5 .6-6.3z"/>
      <text class="contact-line" x="63" y="13.5">+1 555 014 2290</text>
      <text class="contact-line" x="63" y="34.5">+1 555 014 2290</text>
    </g>

    <!-- Web / email -->
    <g class="contact-row" transform="translate(397.5 264)">
      <rect class="icon-box" width="36" height="36"/>
      <circle class="icon-line" cx="18" cy="18" r="9.5"/>
      <ellipse class="icon-line" cx="18" cy="18" rx="4.2" ry="9.5"/>
      <line class="icon-line" x1="8.5" y1="18" x2="27.5" y2="18"/>
      <line class="icon-line" x1="10" y1="13" x2="26" y2="13"/>
      <line class="icon-line" x1="10" y1="23" x2="26" y2="23"/>
      <text class="contact-line" x="63" y="13.5">dana@bluemapleholdings.example</text>
      <text class="contact-line" x="63" y="34.5">www.bluemapleholdings.example</text>
    </g>

    <!-- Address -->
    <g class="contact-row" transform="translate(397.5 336)">
      <rect class="icon-box" width="36" height="36"/>
      <path class="icon-glyph" d="M18 7.5c-4 0-7 3-7 6.8 0 4.8 7 13.2 7 13.2s7-8.4 7-13.2c0-3.8-3-6.8-7-6.8zm0 9.6a2.8 2.8 0 1 1 0-5.6 2.8 2.8 0 0 1 0 5.6z"/>
      <text class="contact-line" x="63" y="13.5">YOUR STREET ADDRESS</text>
      <text class="contact-line" x="63" y="34.5">MAIN AVENUE, NY CITY, USA</text>
    </g>
  </g>
</svg>
</body>
</html>
```